Harbor Panel Works website for creative design and functionality.

Using Wordpress and creative license, create an exciting attractive and super interesting website concept that is easy to navigate, educational, fun, youthful, funny, colourful, global, appealing to all age groups and most businesses who have a use for SIGNS.
Products offered are electronic signs, illuminated channel letters, non-illuminated flat cut and molded letters, specialty products, Wayfinding, large format digital printing, volume printing, programs, rebranding, illuminated cabinet type signs and illuminated freestanding signs.
Services include design (to which PixelHive could be a link), surveys, permits, installations and maintenance.
National refers to CANADA although USA clients who have requirements in Canada or Canadian clients having requirements in the USA are welcome.
Degree of difficulty here is well appreciated. Winner will be selected on basis of creative appeal and uniqueness as well as the designer being able and willing to provide a turnkey service to get the site up and running with or without the help of a lead website designer in Canada.
Domain is harborpanelworks.ca primary and harborpanelworks.com secondary.
Logo exists. Flow chart concept exists. Intent outline exists.
Site should include galleries, Q & A, ugly or funny signs international encouraging global participation, monitored forum for praise and constructive criticism.
HPW works for the client. Objective is to provide premium quality products of ALL TYPES anywhere, for less than market value, from recognized industry leaders (Links), in a timely manner, with transparency, integrity.
Concept is not new but the difference is degree of honesty, commitment to best value, truthfulness of the statement that 'we work for you'.
Given the challenge of website design, we recognize that a turnkey solution can cost us thousands. In an effort to be consistent with our high client standards, we also intend to be extremely loyal and honest and appreciative of the competition winner over the long term as well as anyone who 'tied' or came close second.
To this end, we feel that $500.00 US is a fair incentive to a competition winner whose 'brainchild' is used in whole or in part with two revisions. To be fair to ourselves, we would not be expected to pay anything if the competition generates nothing that excites us. We will work with PixelHive to define that.
As with our future clients, we will be fair, not greedy and honest in our dealings with vendors including designers who want to work with us moving forward. Your excitement will show in your work. Hopefully, our excitement is evident and contagious.
It is not in our best interest nor Pixelhive's best interest to make the contest entries public information due to what we perceive as being a unique competitive template to virtual sign supply. It is suggested that promotion of the creative material produced by entrants be limited to the home page and not the detailed inner 'beauty' of the concept.
I will provide all competitors with all answers to any questions that come up so that a fair playing field is created.
Thank You,
Roy

Target Market(s)

See general info below

Number of Pages Required

5+ page

Font styles to use
Sans Serif

Requirements
Must have
• Defining your business
• 1. Who is your target market?
• Target market is National, Regional and Local entities who buy signs. Targets are retailers, developers, project managers landlords, marketing personnel, Architects, designers and builder.
• 2. What is the overall purpose of your business?
• To do a better job than the conventional sign shop. Better response, better pricing, better communication, better value.
• 3. What distinguishes you from your competitors?
• HPW does not manufacture. We rely on experienced ‘Links’ to provide quality products, preproduction services like surveys and permits, field services like installation and service.
• 4. Who are your major competitors?
• All sign manufacturers are our competitors. Major competitors are those who do multiple locations or program selling. That said, most sign companies have such accounts. Our Links are also our competitors to some degree although we would respect their relationship under normal conditions.
• 6. What are 3 of your businesses strengths?
• Industry relationships (links), knowledge (25 and 40 years of industry experience respectively), existing contact lists of potential clients
• 7. What are the top 3 business values? We work for the client and pride ourselves on our honesty, transparency and integrity
• 8. Do you have a mission statement? If so please include.
• 9. What is your primary offering?
• Illuminated and non-illuminated channel letters, non-illuminated flat cut and molded and specialty letters, electronic signs, large format digital printing. Freestanding signs, illuminated and non-illuminated cabinet signs (wall signs)
• 10. What is your second offering?
• Design, survey, permits, installation and service and to be treated
• 11. What do your customers want?
• Customers want to be treated fairly. They want to be informed and involved (good communications). They want products on time and on budget and right the first time.
• 12. What is the “Emotional Appeal” you want to establish? The feeling you want to come across. In your text, images and graphics?
• Relaxed, excitement, comfort, calm, humour, seriousness, educational, health , confidence, professionalism, knowledgeable
• Marketing and establishing your brand?
• Brand + Marketing + Consistency = CUSTOMERS
• 1. What are some images that best reflect your company brand? ( list three or more)
• Professional. Knowledgeable, loyal, trustworthy, new, positive, confident, artistic, talented, devoted
• 2. What are some colors that best represent your company?
• Multi-color images with pizzaz. Back for nighttime, white for daytime, red for Canadian
• 3. What is your tagline? If you don’t have a tagline please keep these points in mind when creating a tagline. a. Make it quick and easy to say
• b. Try not to go beyond six words. (little words like “the“, and “and” don’t count)
• c. Something that rolls of your tongue and straight into your customer’s memory.
• d. Make sure it provides information.
• HARBOR PANEL WORKS WHERE EXPERIENCE COMES TOGETHER
• Creating your Website
• Please keep in mind that a website can be done in stages. Not everything has to be done before your website goes live. You can add details and blogs, and newsletters as you see fit. Please indicate whether you will need any of these items now or in the future phases of your site.
• 1. Home page think “HOOK” your home page is everything and it’s critical that you instantly hook visitors. Don’t rule out Q&A, the promise of freebies or interesting tips.
• Yes. I want Q & A, ugly and interesting sign gallery from public input, occasional time limited specials for supply of product
• 2. Will you be writing your own content or provide information for us to write it?
• We will work together to create content that we both feel is perfect
• 3. If you are writing your own content will you have someone proof read and edit your content for search engine optimization or will you need us to perform that task?
• You two
• 4. Will you need PayPal on your website?
• No. I have credit card payment capability on our invoices.
• 5. How often will your website need to be updated?
• Weekly hopefully
• 6. Are you thinking of updating your own website?
• Yes
• 7. Will you need a log in account with passwords set up for each customer?
• No
• 8. Will you need a newsletter program for promotions and valuable information? (remember these take time and skill)
• No
• 9. Will you be blogging? (do you have enough information to continue weekly or monthly)
• I don’t think so. I would like to use the Q & A format for that if possible
• 10. How many email accounts will you need to have set up?
• Four should be fine. Two at first
• 11. Will there be any forms on your site and if so how many?
• Quote request form on each product page. Custom order form on Tundra page and maybe the channel letter depot page. We will need a form for submission of photos and artwork (drop box) with file types defined. Design request form with fee schedule
• 12. Will there be a photo gallery and if so how many?
• Yes and several. One for each product. One for for ugly and funny. One for completed HPW projects. Eight to ten.
• 13. Will you need an appointment program for clients to make appointments?
• Yes.
• 14. Do you have a logo?
• Yes
• 15. Do you have an existing website?
• No
• 16. Do you have existing marketing material?
• No BUT each product link (wholesalers) have marketing material and we have permission to use their site content. Eg. Orbo catalog can be downloaded and printed.
• ’
• I do like the static header where viewer has the logo and menu in front of them no matter where they are on the site.
• I don’t like the ‘hamburger’ icon for menu selection – something more personal.
• I like a welcoming atmosphere. Hello. Welcome.
• I would like a glossary of terms page
• Definitely want to encourage ANY questions from ANYBODY that we can respond to with or without research and hence develop and promote FAQ
Nice to have
• See must haves

```html
<!DOCTYPE html>
<html lang="en">
<head>
<meta charset="utf-8">
<title>Harbor Panel Works</title>
<link href="https://fonts.googleapis.com/css2?family=Montserrat:wght@400;500;600;700&display=swap" rel="stylesheet">
<style>
:root{
  --red:#d0312d;
  --red-dark:#b3231f;
  --gold:#f5c518;
  --ink:#1c1c1c;
  --dark:#161616;
  --text:#333;
  --muted:#8a8a8a;
  --light:#f4f4f4;
  --white:#fff;
}
*{margin:0;padding:0;box-sizing:border-box}
html,body{width:1200px;height:3327px;overflow:hidden}
body{font-family:'Montserrat',Arial,sans-serif;color:var(--text);background:var(--white);position:relative}
section,header,footer{position:absolute;left:0;width:1200px}
.abs{position:absolute}

/* header */
.site-header{top:0;height:96px;background:var(--white)}
.brand{left:78px;top:26px;display:flex;align-items:center;gap:12px}
.brand-mark{width:34px;height:34px;background:var(--red)}
.brand-name{font-size:17px;font-weight:700;letter-spacing:2px;color:var(--ink);line-height:1}
.main-nav{left:430px;top:40px;display:flex;gap:34px;font-size:10.5px;font-weight:600;letter-spacing:.5px;color:#444;text-transform:uppercase}
.main-nav .active{color:var(--red)}
.main-nav .drop::after{content:" \2304";font-size:9px}
.quote-btn{left:969px;top:29px;width:152px;height:36px;border:2px solid var(--red);border-radius:18px;font-size:10.5px;font-weight:600;color:var(--red);display:flex;align-items:center;justify-content:center;letter-spacing:.5px}

/* hero */
.hero{top:96px;height:439px;background:linear-gradient(120deg,#1c3f94 0%,#2a63c4 22%,#e46b86 42%,#2b2f6e 58%,#19b8c4 78%,#2a54b7 100%)}
.hero-frame{left:326px;top:161px;width:30px;height:30px;border-left:2px solid #fff;border-top:2px solid #fff}
.hero-title{left:0;width:1200px;text-align:center;top:186px;font-size:36px;font-weight:600;letter-spacing:5px;color:#fff}
.hero-tag{left:0;width:1200px;text-align:center;top:234px;font-size:14px;font-weight:600;letter-spacing:2px;color:#fff}

/* stats band */
.stats{top:535px;height:159px;background:var(--red)}
.stats-map{left:160px;top:18px;width:200px;height:124px;background:var(--red-dark);border-radius:40px 10px 60px 20px}
.stats-num{left:200px;top:48px;font-size:50px;font-weight:500;color:#2a0f0f}
.stats-chevron{left:346px;top:22px}
.stats-title{left:410px;top:47px;font-size:19px;font-weight:500;color:#fff}
.stats-title b{color:var(--gold);font-weight:600}
.stats-copy{left:410px;top:78px;width:370px;font-size:11.5px;line-height:18px;color:#fbe6e6}
.dark-btn{left:915px;top:58px;width:128px;height:38px;background:var(--ink);border-radius:19px;color:#fff;font-size:10px;font-weight:600;display:flex;align-items:center;justify-content:center;letter-spacing:.5px}

/* section headings */
.sec-head{font-size:25px;font-weight:500;letter-spacing:1px;text-transform:uppercase;padding:22px 0 0 24px}
.sec-head::before{content:"";position:absolute;left:0;top:0;width:24px;height:34px;border-left:2px solid var(--red);border-top:2px solid var(--red)}

/* about */
.about{top:694px;height:276px}
.about .sec-head{left:484px;top:48px;color:var(--ink)}
.about-copy{left:235px;top:103px;width:730px;text-align:center;font-size:12.5px;line-height:18px;color:#666}
.text-link{font-size:10px;font-weight:600;letter-spacing:.5px;color:#333}
.about .text-link{left:0;width:1200px;text-align:center;top:189px}

/* products */
.products{top:970px;height:543px;background:var(--dark)}
.products .sec-head{left:155px;top:60px;color:#fff}
.dots{left:1015px;top:80px;display:flex;gap:4px}
.dots i{width:7px;height:7px;border-radius:50%;background:var(--red);opacity:.55}
.dots i:first-child{opacity:1}
.tile{top:126px;width:300px;height:301px}
.tile-1{left:0;background:radial-gradient(circle at 50% 45%,#d0457a,#5a1636 70%,#2a0a1c)}
.tile-2{left:300px;background:linear-gradient(#2c2c2c,#111);border:4px solid #6a7d86}
.tile-3{left:600px;background:radial-gradient(circle at 50% 40%,#3a3a3a,#151515)}
.tile-4{left:900px;background:linear-gradient(135deg,#4c5157,#2f3338)}
.tile-2 .tile-title{left:0;width:292px;text-align:center;top:114px;color:#fff;font-size:16px;font-weight:600;line-height:20px}
.tile-2 .red-btn{left:82px;top:168px}
.red-btn{width:128px;height:30px;background:var(--red);border-radius:15px;color:#fff;font-size:10px;font-weight:600;display:flex;align-items:center;justify-content:center;letter-spacing:.5px}
.pager{left:0;width:1200px;top:456px;display:flex;justify-content:center;align-items:center;gap:90px;font-size:10px;font-weight:600;color:#fff;letter-spacing:.5px}
.arrow{font-size:16px;color:#fff}
.arrow.next{color:var(--red)}

/* services */
.services{top:1513px;height:455px}
.services .sec-head{left:486px;top:40px;color:var(--ink)}
.service{top:146px;width:200px;text-align:center}
.service svg{display:block;margin:0 auto}
.service h3{margin-top:22px;font-size:15px;font-weight:600;color:var(--ink)}
.service p{margin-top:12px;font-size:11.5px;line-height:17px;color:#888}
.outline-btn{left:532px;top:362px;width:136px;height:34px;border:2px solid var(--red);border-radius:17px;color:var(--red);font-size:10px;font-weight:600;display:flex;align-items:center;justify-content:center;letter-spacing:.5px}

/* recent work */
.work{top:1968px;height:679px;background:var(--light)}
.work .sec-head{left:475px;top:44px;color:var(--ink)}
.cell{position:absolute}
.w-sign{left:155px;top:115px;width:444px;height:222px;background:linear-gradient(135deg,#d9d9d9,#8a8f94 60%,#4a4d52)}
.w-hover{left:599px;top:115px;width:222px;height:222px;background:var(--red);border:5px solid #e6504c;display:flex;flex-direction:column;align-items:center;justify-content:center;color:#fff;font-size:13px;text-align:center;line-height:18px}
.w-poster{left:821px;top:115px;width:222px;height:222px;background:linear-gradient(#7d8794,#3e444b)}
.w-casino{left:155px;top:337px;width:222px;height:222px;background:radial-gradient(circle at 50% 45%,#d0457a,#5a1636 70%,#2a0a1c)}
.w-station{left:377px;top:337px;width:222px;height:222px;background:linear-gradient(135deg,#565b61,#33373c)}
.w-fascia{left:599px;top:337px;width:444px;height:222px;background:linear-gradient(160deg,#cfcfcf 0%,#3b3e42 45%,#2a2c30 100%)}
.work .pager{top:591px;color:#333}
.work .arrow{color:#999}

/* partners */
.partners{top:2647px;height:266px}
.partners .sec-head{left:155px;top:54px;color:var(--ink)}
.badge{top:162px;height:50px;border-radius:6px;background:#e7e7e7}

/* footer */
.site-footer{top:2913px;height:414px;background:#1d1d1d}
.foot-info{left:155px;top:70px;color:#ddd}
.foot-info h4{font-size:14px;font-weight:600;color:#fff;margin-bottom:22px}
.foot-info p{font-size:11.5px;line-height:17px}
.foot-info .label{font-size:11.5px;margin-top:16px;color:#ccc}
.foot-info .phone{font-size:14px}
.socials{display:flex;gap:6px;margin-top:8px}
.socials i{width:22px;height:22px;border-radius:50%;background:var(--red)}
.legal{margin-top:22px;font-size:11.5px}
.legal-links{font-size:9.5px;margin-top:6px}
.legal-links span{color:var(--red)}
.foot-quote{left:599px;top:0;width:601px;height:414px;background:linear-gradient(170deg,#5b6064 0%,#3f4447 50%,#2b2e30 100%)}
.foot-quote h4{position:absolute;left:64px;top:70px;font-size:14px;font-weight:600;color:#fff}
.field{position:absolute;height:32px;border:1px solid #aeb4b8;color:#e6e6e6;font-size:11px;padding:8px 12px}
.send{position:absolute;left:64px;top:303px;width:120px;height:34px;background:var(--red);border-radius:17px;color:#fff;font-size:10px;font-weight:600;display:flex;align-items:center;justify-content:center;gap:6px}
.to-top{position:absolute;left:1110px;top:325px;width:0;height:0;border-left:10px solid transparent;border-right:10px solid transparent;border-bottom:12px solid var(--red)}
</style>
</head>
<body>

<header class="site-header">
  <div class="abs brand"><span class="brand-mark"></span><span class="brand-name">HARBOR PANEL WORKS</span></div>
  <nav class="abs main-nav">
    <span class="active">Home</span><span>About Us</span><span class="drop">Service</span><span class="drop">Products</span><span>Gallery</span><span>Contact Us</span>
  </nav>
  <div class="abs quote-btn">REQUEST A QUOTE</div>
</header>

<section class="hero" role="img" aria-label="Colourful abstract geometric shapes in blue, pink and teal">
  <div class="abs hero-frame"></div>
  <h1 class="abs hero-title">HARBOR PANEL WORKS</h1>
  <p class="abs hero-tag">WHERE EXPERIENCE COMES TOGETHER</p>
</section>

<section class="stats">
  <div class="abs stats-map" role="img" aria-label="Map of North America"></div>
  <div class="abs stats-num">3.560</div>
  <svg class="abs stats-chevron" width="30" height="115" viewBox="0 0 30 115"><polyline points="2,0 28,57 2,115" fill="none" stroke="#e87470" stroke-width="2"/></svg>
  <div class="abs stats-title">Competed <b>Projects</b></div>
  <p class="abs stats-copy">Lorem Impsum has been the industry's standard dummy text printing and typesetting</p>
  <div class="abs dark-btn">GET STARTED</div>
</section>

<section class="about">
  <h2 class="abs sec-head">Who We Are</h2>
  <p class="abs about-copy">Lorem Ipsum is simply dummy text of the printing and typesetting industry been the industry's standard dummy text ever since the 1500s, when an unknown printer took a galley of type and scrambled it to make a type specimen book.</p>
  <div class="abs text-link">DISCOVER ABOUT US</div>
</section>

<section class="products">
  <h2 class="abs sec-head">Products</h2>
  <div class="abs dots"><i></i><i></i><i></i></div>
  <div class="abs tile tile-1" role="img" aria-label="Illuminated casino style sign glowing at night"></div>
  <div class="abs tile tile-2" role="img" aria-label="Freestanding poster sign at dusk">
    <div class="abs tile-title">Illuminated<br>Freestanding Signs</div>
    <div class="abs red-btn">EXPLORE MORE</div>
  </div>
  <div class="abs tile tile-3" role="img" aria-label="Brand sign on dark textured wall"></div>
  <div class="abs tile tile-4" role="img" aria-label="Printed stationery set in red and white"></div>
  <div class="abs pager"><span class="arrow">&#8592;</span><span>ALL PRODUCTS</span><span class="arrow next">&#8594;</span></div>
</section>

<section class="services">
  <h2 class="abs sec-head">What We Do</h2>
  <div class="abs service" style="left:157px">
    <svg width="70" height="66" viewBox="0 0 70 66" fill="none" stroke="#999" stroke-width="1.6"><path d="M35 8 L22 34 L35 60 L48 34 Z"/><circle cx="35" cy="34" r="4"/><line x1="35" y1="8" x2="35" y2="30"/><line x1="8" y1="8" x2="62" y2="8"/><rect x="31" y="4" width="8" height="8"/><circle cx="6" cy="8" r="3"/><circle cx="64" cy="8" r="3"/></svg>
    <h3>Design</h3>
    <p>Lorem Ipsum is simply dummy text of the printing &amp; typesetting industry</p>
  </div>
  <div class="abs service" style="left:386px">
    <svg width="70" height="66" viewBox="0 0 70 66" fill="none" stroke="#d0312d" stroke-width="1.8"><rect x="10" y="8" width="50" height="36"/><line x1="6" y1="8" x2="64" y2="8"/><circle cx="28" cy="26" r="8"/><path d="M28 18 V26 H36"/><line x1="44" y1="38" x2="44" y2="30"/><line x1="49" y1="38" x2="49" y2="24"/><line x1="54" y1="38" x2="54" y2="27"/><line x1="35" y1="44" x2="24" y2="62"/><line x1="35" y1="44" x2="46" y2="62"/></svg>
    <h3>Surveys</h3>
    <p>Lorem Ipsum is simply dummy text of the printing &amp; typesetting industry</p>
  </div>
  <div class="abs service" style="left:614px">
    <svg width="70" height="66" viewBox="0 0 70 66" fill="none" stroke="#999" stroke-width="1.6"><path d="M14 4 H42 L52 14 V62 H14 Z"/><path d="M42 4 V14 H52"/><line x1="22" y1="26" x2="40" y2="26"/><line x1="22" y1="34" x2="40" y2="34"/><line x1="22" y1="42" x2="34" y2="42"/><path d="M40 50 L62 24 L66 28 L44 54 L38 56 Z"/></svg>
    <h3>Permits</h3>
    <p>Lorem Ipsum is simply dummy text of the printing &amp; typesetting industry</p>
  </div>
  <div class="abs service" style="left:840px">
    <svg width="70" height="66" viewBox="0 0 70 66" fill="none" stroke="#999" stroke-width="1.6"><line x1="12" y1="4" x2="12" y2="62"/><line x1="12" y1="10" x2="58" y2="10"/><line x1="26" y1="10" x2="26" y2="20"/><line x1="50" y1="10" x2="50" y2="20"/><rect x="20" y="20" width="38" height="24"/></svg>
    <h3>Installations</h3>
    <p>Lorem Ipsum is simply dummy text of the printing &amp; typesetting industry</p>
  </div>
  <div class="abs outline-btn">EXPLORE MORE</div>
</section>

<section class="work">
  <h2 class="abs sec-head">Recent Work</h2>
  <div class="cell w-sign" role="img" aria-label="Round hanging shop sign on a building wall"></div>
  <div class="cell w-hover"><svg width="14" height="14" viewBox="0 0 14 14" stroke="#fff" stroke-width="1.5"><line x1="2" y1="12" x2="12" y2="2"/><polyline points="6,2 12,2 12,8" fill="none"/></svg><span style="margin-top:10px">Lorem Ipsum is simply<br>dummy text</span></div>
  <div class="cell w-poster" role="img" aria-label="Roadside billboard poster on an overcast street"></div>
  <div class="cell w-casino" role="img" aria-label="Illuminated casino style sign"></div>
  <div class="cell w-station" role="img" aria-label="Stationery set in red and white"></div>
  <div class="cell w-fascia" role="img" aria-label="Building fascia with lettered sign and yellow emblem"></div>
  <div class="abs pager"><span class="arrow">&#8592;</span><span>VIEW ALL PHOTO</span><span class="arrow">&#8594;</span></div>
</section>

<section class="partners">
  <h2 class="abs sec-head">Our Partners</h2>
  <div class="abs badge" style="left:80px;width:138px"></div>
  <div class="abs badge" style="left:295px;width:64px"></div>
  <div class="abs badge" style="left:440px;width:140px"></div>
  <div class="abs badge" style="left:634px;width:114px"></div>
  <div class="abs badge" style="left:840px;width:64px"></div>
  <div class="abs badge" style="left:982px;width:140px"></div>
</section>

<footer class="site-footer">
  <div class="abs foot-info">
    <h4>Harbor Panel Works</h4>
    <p>58 Quay Lane, Harbour Row,<br>Halifax, NS-2210</p>
    <p class="label">Contact Us</p>
    <p class="phone">+1 (902) 555-0187</p>
    <p>info@harborpanelworks.com</p>
    <p class="label">Get Social</p>
    <div class="socials"><i></i><i></i><i></i><i></i><i></i></div>
    <p class="legal">&copy; Copyright 2017 Harbor Panel Works.</p>
    <p class="legal-links"><span>TERMS OF USE</span> &nbsp;/&nbsp; PRIVACY POLICY</p>
  </div>
  <div class="abs foot-quote" role="img" aria-label="Misty countryside road with guard posts">
    <h4>Request a Quote</h4>
    <div class="field" style="left:64px;top:106px;width:184px">Name</div>
    <div class="field" style="left:260px;top:106px;width:184px">Email</div>
    <div class="field" style="left:64px;top:148px;width:184px">Phone</div>
    <div class="field" style="left:260px;top:148px;width:184px">Select Project &nbsp;&nbsp;&nbsp;&nbsp;&nbsp;&nbsp;&nbsp;&nbsp;&nbsp;&nbsp;&nbsp;&nbsp;&#8964;</div>
    <div class="field" style="left:64px;top:190px;width:380px;height:100px">Type your Message</div>
    <div class="send"><svg width="11" height="11" viewBox="0 0 11 11"><path d="M0 5 L11 0 L7 11 L5 6 Z" fill="#fff"/></svg>SEND</div>
    <div class="to-top"></div>
  </div>
</footer>

</body>
</html>
```